KORVO RENEWABLES

New business B2B Energy Renewables website.
Please refer to our competitor https://www.tarnex42.co.uk/ for a similar website.

Need extra days to review

```html
<!DOCTYPE html>
<html lang="en">
<head>
<meta charset="utf-8">
<title>Korvo Renewables</title>
<link href="https://fonts.googleapis.com/css2?family=Rubik:wght@400;500;600;700&family=Montserrat:wght@400;500;600;700&display=swap" rel="stylesheet">
<style>
:root{
  --navy:#1b3482;
  --navy-deep:#132a6e;
  --blue:#2e6ad8;
  --ink:#1d1d1f;
  --text:#444a55;
  --pale:#eef2fb;
  --line:#c9cfdc;
  --white:#ffffff;
}
*{box-sizing:border-box;margin:0;padding:0}
html,body{width:1200px;height:4231px;overflow:hidden}
body{position:relative;background:var(--white);font-family:'Montserrat',sans-serif;color:var(--text)}
.abs{position:absolute}
h1,h2,h3{font-family:'Rubik',sans-serif}

/* header */
.header{position:absolute;left:0;top:0;width:1200px;height:95px;background:var(--white);z-index:5}
.brand{position:absolute;display:flex;align-items:center;gap:10px;font-family:'Rubik',sans-serif;font-weight:700;letter-spacing:2px;white-space:nowrap}
.brand .mark{width:26px;height:26px;background:var(--navy);flex:none}
.header .brand{left:112px;top:32px;font-size:20px;color:var(--navy)}
.contact-item{position:absolute;top:14px;display:flex;align-items:center;gap:10px}
.contact-item .ico{width:44px;height:44px;border-radius:50%;background:var(--navy);border:3px solid #c8d4f2;display:flex;align-items:center;justify-content:center}
.contact-item small{display:block;font-size:13px;color:var(--ink)}
.contact-item strong{display:block;font-size:16px;color:var(--blue);font-weight:700}
.nav{position:absolute;left:386px;top:75px;width:814px;height:43px;z-index:6}
.nav svg{position:absolute;left:0;top:0}
.nav ul{position:absolute;left:0;top:0;list-style:none;font-size:13px;color:var(--ink)}
.nav li{position:absolute;top:15px;white-space:nowrap}
.nav li.active{color:var(--blue)}
.nav li.active::after{content:"";position:absolute;left:0;right:0;bottom:-9px;height:2px;background:var(--blue)}

/* hero */
.hero{position:absolute;left:0;top:95px;width:1200px;height:622px;z-index:1}
.hero .photo{position:absolute;inset:0;background:linear-gradient(180deg,#6f9fd6 0%,#b9d0e6 35%,#9fb0bc 55%,#5b7f3a 75%,#3f6a2a 100%)}
.hero h1{position:absolute;left:0;width:1200px;top:100px;text-align:center;color:var(--white);font-size:33px;line-height:41px;font-weight:700;text-shadow:0 2px 6px rgba(0,0,0,.35)}
.hero p{position:absolute;left:0;width:1200px;top:194px;text-align:center;color:var(--white);font-size:19px;line-height:30px;font-weight:500;text-shadow:0 2px 6px rgba(0,0,0,.35)}
.btn{position:absolute;height:37px;display:flex;font-size:13px;font-weight:700;color:var(--white);letter-spacing:.5px}
.btn span{flex:1;background:var(--blue);display:flex;align-items:center;padding-left:14px}
.btn i{width:37px;background:var(--navy-deep);display:flex;align-items:center;justify-content:center}
.hero-arrow{position:absolute;top:288px;width:60px;height:60px;border:2px solid rgba(255,255,255,.9);border-radius:50%;display:flex;align-items:center;justify-content:center}
.dots{position:absolute;top:584px;left:572px;display:flex;gap:5px}
.dots b{width:10px;height:10px;border-radius:50%;border:1.5px solid #fff}
.dots b.on{background:#fff}

/* media blocks */
.media{position:absolute}
.media .frame{position:absolute;border:2px solid var(--blue)}
.media .fill{position:absolute}
.eyebrow{font-size:17px;color:var(--navy);font-weight:600;letter-spacing:1px}
.para{font-size:14px;line-height:24.6px;color:var(--text)}

/* services */
.services{position:absolute;left:0;top:1254px;width:1200px;height:478px;background:var(--pale)}
.services h2{position:absolute;left:0;width:1200px;top:70px;text-align:center;font-size:33px;font-weight:500;color:var(--ink)}
.services .rule{position:absolute;left:553px;top:125px;width:94px;height:4px;background:var(--navy)}
.card{position:absolute;top:161px;width:186px;height:230px;background:#f6f7f9;box-shadow:0 2px 8px rgba(20,40,90,.15);text-align:center}
.card svg{position:absolute;left:53px;top:48px}
.card h3{position:absolute;left:0;right:0;top:172px;font-size:17px;font-weight:500;color:var(--ink);letter-spacing:.3px}

/* features */
.feature h2{position:absolute;font-size:33px;font-weight:500;color:var(--navy);white-space:nowrap}
.feature .divider{position:absolute;width:200px;height:2px;background:var(--line)}
.feature .lead{position:absolute;font-size:20px;line-height:31px;font-weight:600;color:var(--blue)}
.feature .para{position:absolute;width:470px}

/* contact */
.contact{position:absolute;left:0;top:3165px;width:1200px;height:717px;background:linear-gradient(180deg,#23418f 0%,#2a4a99 50%,#1f3c88 100%)}
.contact .panel{position:absolute;left:243px;top:225px;width:714px;height:386px;background:rgba(255,255,255,.08)}
.contact h2{position:absolute;left:0;width:1200px;top:78px;text-align:center;font-size:33px;font-weight:500;color:var(--white)}
.contact .rule{position:absolute;left:553px;top:130px;width:94px;height:4px;background:var(--white)}
.contact p{position:absolute;left:0;width:1200px;top:150px;text-align:center;font-size:20px;line-height:31px;font-weight:600;color:var(--white)}
.field{position:absolute;background:var(--white);border-bottom-right-radius:34px;display:flex;align-items:center;gap:10px;padding-left:12px;font-size:12px;color:var(--ink)}
.field.msg{align-items:flex-start;padding-top:14px;border-bottom-right-radius:60px}

/* footer */
.footer{position:absolute;left:0;top:3882px;width:1200px;height:349px;background:var(--navy-deep)}
.footer .brand{left:123px;top:74px;font-size:17px;letter-spacing:1px;color:var(--white)}
.footer .brand .mark{background:var(--white);width:22px;height:22px}
.social{position:absolute;top:156px;width:36px;height:36px;border-radius:50%;border:1.5px solid var(--white)}
.fcol{position:absolute;top:48px}
.fcol h3{font-size:19px;font-weight:500;color:var(--white);letter-spacing:.5px;padding-bottom:10px;border-bottom:2px solid rgba(255,255,255,.5);min-width:120px;white-space:nowrap}
.fcol ul{list-style:none;margin-top:18px}
.fcol li{font-size:11px;color:var(--white);line-height:24px;letter-spacing:.3px;white-space:nowrap}
.legal{position:absolute;top:300px;font-size:11px;color:var(--white);white-space:nowrap}
.to-top{position:absolute;left:1107px;top:244px;width:44px;height:44px;border-radius:50%;background:var(--white);display:flex;align-items:center;justify-content:center}
</style>
</head>
<body>

<header class="header">
  <div class="brand"><span class="mark"></span>KORVO RENEWABLES</div>
  <div class="contact-item" style="left:467px">
    <div class="ico"><svg width="20" height="20" viewBox="0 0 24 24"><path d="M6.6 10.8a15.2 15.2 0 0 0 6.6 6.6l2.2-2.2a1 1 0 0 1 1-.25 11.4 11.4 0 0 0 3.6.57 1 1 0 0 1 1 1V20a1 1 0 0 1-1 1A17 17 0 0 1 3 4a1 1 0 0 1 1-1h3.5a1 1 0 0 1 1 1c0 1.25.2 2.45.57 3.57a1 1 0 0 1-.25 1z" fill="#fff"/></svg></div>
    <div><small>Call Now:</small><strong>+1 (555) 013 2290</strong></div>
  </div>
  <div class="contact-item" style="left:750px">
    <div class="ico"><svg width="20" height="20" viewBox="0 0 24 24"><rect x="3" y="6" width="18" height="12" rx="1" fill="#fff"/><path d="M3 6l9 7 9-7" stroke="#1b3482" stroke-width="1.8" fill="none"/></svg></div>
    <div><small>Email Us:</small><strong>info@korvorenewables.com</strong></div>
  </div>
</header>

<nav class="nav">
  <svg width="814" height="43"><path d="M0 43 L33 2 H814 V43 Z" fill="#fff"/><path d="M0 43 L33 2 H814" stroke="#1b3482" stroke-width="4" fill="none"/></svg>
  <ul>
    <li class="active" style="left:103px">Home</li>
    <li style="left:179px">About Us</li>
    <li style="left:276px">Services</li>
    <li style="left:367px">Solutions</li>
    <li style="left:464px">Sectors</li>
    <li style="left:550px">Case Studies</li>
    <li style="left:670px">More</li>
  </ul>
</nav>

<section class="hero">
  <div class="photo" role="img" aria-label="City skyline with wind turbines and solar panels on green grass"></div>
  <h1>THE FUTURE IS RENEWABLE ENERGY,<br>GREEN ENERGY, SUSTAINABILITY.</h1>
  <p>Perspiciatisunde omnisiste natuserorsit voluptatem<br>accusantium doloremque laudantium totamrem.</p>
  <a class="btn" style="left:515px;top:268px;width:170px"><span>GET STARTED</span><i><svg width="14" height="12" viewBox="0 0 14 12"><path d="M1 6h11M8 2l4 4-4 4" stroke="#fff" stroke-width="1.6" fill="none"/></svg></i></a>
  <div class="hero-arrow" style="left:21px"><svg width="22" height="18" viewBox="0 0 22 18"><path d="M21 9H2M9 2L2 9l7 7" stroke="#fff" stroke-width="2" fill="none"/></svg></div>
  <div class="hero-arrow" style="left:1109px"><svg width="22" height="18" viewBox="0 0 22 18"><path d="M1 9h19M13 2l7 7-7 7" stroke="#fff" stroke-width="2" fill="none"/></svg></div>
  <div class="dots"><b></b><b class="on"></b><b></b><b></b></div>
</section>

<section class="welcome">
  <div class="media" style="left:103px;top:796px;width:496px;height:371px">
    <div class="frame" style="left:0;top:0;width:490px;height:371px;border-bottom-left-radius:60px;border-right:none"></div>
    <div class="fill" style="left:9px;top:8px;width:487px;height:363px;border-bottom-left-radius:56px;background:linear-gradient(180deg,#3f7ed8 0%,#9cc2ec 40%,#2a4c9c 62%,#1d3578 100%)" role="img" aria-label="Solar panel field with wind turbines under blue sky"></div>
  </div>
  <div class="eyebrow abs" style="left:612px;top:797px">Welcome to</div>
  <h2 class="abs" style="left:612px;top:820px;font-size:33px;font-weight:500;color:var(--ink)">Korvo Renewables</h2>
  <p class="para abs" style="left:612px;top:873px;width:466px;text-align:justify">Perspiciatis undeloseikla omnis iste natus error sit voluptatem accusantium doloremque laudalse ontium, totam rem aperiam, eaque ipsa quae ab illo inventore veritatis et quasi architecto beatae vitae dicta suntoaseijdskl explicabo. Nemo enim ipsam voluptatem quia voluptas sit aspernatur aut odit aut fugit, sed quia consequuntur magni dolores eos qui ratione voluptatem sequi nesciunt. Neque porro quisquam est, qui dolorem ipsum quia dolor sit amet, consectetur, adipisci velit, sed quia non numquam eius modi tempora.</p>
  <a class="btn" style="left:612px;top:1124px;width:171px"><span>LEARN MORE</span><i><svg width="14" height="12" viewBox="0 0 14 12"><path d="M1 6h11M8 2l4 4-4 4" stroke="#fff" stroke-width="1.6" fill="none"/></svg></i></a>
</section>

<section class="services">
  <h2>Our Services</h2>
  <div class="rule"></div>
  <div class="card" style="left:110px">
    <svg width="80" height="90" viewBox="0 0 80 90" fill="none" stroke="#1b3482" stroke-width="2.4"><rect x="26" y="2" width="40" height="24" rx="12"/><path d="M36 26l-4 7 10-7"/><path d="M36 11h20M36 17h14"/><circle cx="20" cy="52" r="9"/><path d="M4 84c0-12 7-20 16-20s16 8 16 20z"/><circle cx="58" cy="52" r="9"/><path d="M42 84c0-12 7-20 16-20s16 8 16 20z"/></svg>
    <h3>CONSULTING</h3>
  </div>
  <div class="card" style="left:309px">
    <svg width="80" height="90" viewBox="0 0 80 90" fill="none" stroke="#1b3482" stroke-width="2.4"><rect x="4" y="14" width="62" height="60"/><path d="M4 22h62"/><path d="M70 8l6 6-36 36-8 2 2-8z"/><path d="M30 84h46L76 56z"/><path d="M66 70h6"/></svg>
    <h3>DESIGN</h3>
  </div>
  <div class="card" style="left:507px">
    <svg width="80" height="90" viewBox="0 0 80 90" fill="none" stroke="#1b3482" stroke-width="2.4"><path d="M4 84h72"/><rect x="10" y="58" width="10" height="26"/><rect x="28" y="48" width="10" height="36"/><rect x="46" y="40" width="10" height="44"/><rect x="64" y="28" width="10" height="56"/><path d="M6 46L30 28l12 8 26-22" stroke="#2e6ad8"/><path d="M60 12h10v10" stroke="#2e6ad8"/></svg>
    <h3>FINANCE</h3>
  </div>
  <div class="card" style="left:706px">
    <svg width="80" height="90" viewBox="0 0 80 90" fill="none" stroke="#1b3482" stroke-width="2.4"><path d="M48 4v14h12V4c6 3 8 9 6 15l-4 6v30l4 6c2 6 0 12-6 15V72H48v14c-6-3-8-9-6-15l4-6V35l-4-6c-2-6 0-12 6-15z"/><path d="M4 42h16v26H4z"/><path d="M20 46h14c4 0 6 3 6 6s-2 6-6 6H20"/></svg>
    <h3>INSTALLATION</h3>
  </div>
  <div class="card" style="left:903px">
    <svg width="80" height="90" viewBox="0 0 80 90" fill="none" stroke="#1b3482" stroke-width="2.4"><circle cx="48" cy="26" r="8" stroke="#2e6ad8"/><path d="M48 6v6M48 40v6M28 26h6M62 26h6M34 12l4 4M58 36l4 4M34 40l4-4M58 16l4-4" stroke="#2e6ad8"/><path d="M4 54h12v26H4z"/><path d="M16 58h20c4 0 6 3 6 6H30M16 76h32l22-16c-2-4-6-4-10-2l-14 8"/></svg>
    <h3>MAINTENANCE</h3>
  </div>
</section>

<section class="feature">
  <h2 style="left:110px;top:1820px">Various renewables offered</h2>
  <p class="lead" style="left:110px;top:1908px;width:480px">Kaojs oloaek erspiciatis undeloseikla omnisiste natuserror sivoluptatem accusantium doloremque laudalse ontium.</p>
  <p class="para" style="left:110px;top:2019px">Perspiciatis undeloseikla omnis iste natus error sit voluptatem accusantium doloremque laudalse ontium totam rem aperiam, eaque ipsa quae ab illo inventore veritatisl seokseok Perspiciatis undeloseikla omnis iste natusrspiciatis undeloseikla.</p>
  <a class="btn" style="left:110px;top:2146px;width:170px"><span>LEARN MORE</span><i><svg width="14" height="12" viewBox="0 0 14 12"><path d="M1 6h11M8 2l4 4-4 4" stroke="#fff" stroke-width="1.6" fill="none"/></svg></i></a>
  <div class="media" style="left:598px;top:1814px;width:484px;height:369px">
    <div class="frame" style="left:0;top:0;width:480px;height:369px;border-top-left-radius:60px"></div>
    <div class="fill" style="left:8px;top:0;width:476px;height:362px;border-top-left-radius:56px;background:linear-gradient(90deg,#5d5f62 0%,#b8babc 45%,#d8d9da 70%,#8b8c8e 100%)" role="img" aria-label="White electric car beside a charging station"></div>
  </div>
</section>

<section class="feature">
  <div class="media" style="left:110px;top:2260px;width:484px;height:370px">
    <div class="frame" style="left:4px;top:4px;width:480px;height:366px;border-top-right-radius:60px;border-top:none"></div>
    <div class="fill" style="left:0;top:0;width:478px;height:363px;border-top-right-radius:58px;background:radial-gradient(circle at 48% 48%,#f0c86a 0%,#b08040 18%,#2f4a6e 45%,#182c4a 100%)" role="img" aria-label="Hand holding a glowing light bulb with a seedling and energy symbols"></div>
  </div>
  <h2 style="left:624px;top:2266px">Energy Saving Assessment</h2>
  <div class="divider" style="left:624px;top:2331px"></div>
  <p class="lead" style="left:624px;top:2354px;width:480px">Kaojs oloaek erspiciatis undeloseikla omnisiste natuserror sivoluptatem accusantium doloremque laudalse ontium.</p>
  <p class="para" style="left:624px;top:2465px">Perspiciatis undeloseikla omnis iste natus error sit voluptatem accusantium doloremque laudalse ontium totam rem aperiam, eaque ipsa quae ab illo inventore veritatisl seokseok Perspiciatis undeloseikla omnis iste natusrspiciatis undeloseikla.</p>
  <a class="btn" style="left:624px;top:2592px;width:170px"><span>LEARN MORE</span><i><svg width="14" height="12" viewBox="0 0 14 12"><path d="M1 6h11M8 2l4 4-4 4" stroke="#fff" stroke-width="1.6" fill="none"/></svg></i></a>
</section>

<section class="feature">
  <h2 style="left:110px;top:2713px">Monitoring</h2>
  <div class="divider" style="left:110px;top:2778px"></div>
  <p class="lead" style="left:110px;top:2801px;width:480px">Kaojs oloaek erspiciatis undeloseikla omnisiste natuserror sivoluptatem accusantium doloremque laudalse ontium.</p>
  <p class="para" style="left:110px;top:2912px">Perspiciatis undeloseikla omnis iste natus error sit voluptatem accusantium doloremque laudalse ontium totam rem aperiam, eaque ipsa quae ab illo inventore veritatisl seokseok Perspiciatis undeloseikla omnis iste natusrspiciatis undeloseikla.</p>
  <a class="btn" style="left:110px;top:3039px;width:170px"><span>LEARN MORE</span><i><svg width="14" height="12" viewBox="0 0 14 12"><path d="M1 6h11M8 2l4 4-4 4" stroke="#fff" stroke-width="1.6" fill="none"/></svg></i></a>
  <div class="media" style="left:598px;top:2707px;width:484px;height:369px">
    <div class="frame" style="left:0;top:0;width:480px;height:369px;border-top-left-radius:60px"></div>
    <div class="fill" style="left:8px;top:0;width:476px;height:362px;border-top-left-radius:56px;background:linear-gradient(180deg,#1f5ad8 0%,#6ea0e8 45%,#b86a3a 62%,#2e4f92 78%,#3a5fa8 100%)" role="img" aria-label="Engineer in a hard hat checking a laptop among solar panels and wind turbines"></div>
  </div>
</section>

<section class="contact" role="img" aria-label="Contact section over a faint blue wind farm backdrop">
  <div class="panel"></div>
  <h2>Contact Us</h2>
  <div class="rule"></div>
  <p>Kaojs oloaek erspiciatis undeloseikla omnisiste natuserror sivoluptatem accusantium<br>doloremque laudalse ontium.</p>
  <div class="field" style="left:325px;top:271px;width:266px;height:44px"><svg width="12" height="13" viewBox="0 0 12 13"><circle cx="6" cy="3.5" r="3" fill="#1b3482"/><path d="M0 13c0-4 3-6 6-6s6 2 6 6z" fill="#1b3482"/></svg>First Name</div>
  <div class="field" style="left:607px;top:271px;width:266px;height:44px"><svg width="12" height="13" viewBox="0 0 12 13"><circle cx="6" cy="3.5" r="3" fill="#1b3482"/><path d="M0 13c0-4 3-6 6-6s6 2 6 6z" fill="#1b3482"/></svg>Last Name</div>
  <div class="field" style="left:325px;top:332px;width:266px;height:44px"><svg width="14" height="11" viewBox="0 0 14 11"><rect width="14" height="11" fill="#1b3482"/><path d="M0 0l7 6 7-6" stroke="#fff" stroke-width="1.2" fill="none"/></svg>Email</div>
  <div class="field" style="left:607px;top:332px;width:266px;height:44px"><svg width="13" height="13" viewBox="0 0 24 24"><path d="M6.6 10.8a15.2 15.2 0 0 0 6.6 6.6l2.2-2.2a1 1 0 0 1 1-.25 11.4 11.4 0 0 0 3.6.57 1 1 0 0 1 1 1V20a1 1 0 0 1-1 1A17 17 0 0 1 3 4a1 1 0 0 1 1-1h3.5a1 1 0 0 1 1 1c0 1.25.2 2.45.57 3.57a1 1 0 0 1-.25 1z" fill="#1b3482"/></svg>Phone</div>
  <div class="field msg" style="left:325px;top:392px;width:548px;height:109px"><svg width="12" height="12" viewBox="0 0 12 12"><path d="M1 1l10 10" stroke="#1b3482" stroke-width="2"/></svg>Enter Your Message</div>
  <a class="btn" style="left:515px;top:527px;width:170px"><span>SUBMIT</span><i><svg width="14" height="12" viewBox="0 0 14 12"><path d="M1 6h11M8 2l4 4-4 4" stroke="#fff" stroke-width="1.6" fill="none"/></svg></i></a>
</section>

<footer class="footer">
  <div class="brand"><span class="mark"></span>KORVO RENEWABLES</div>
  <span class="social" style="left:146px"></span>
  <span class="social" style="left:194px"></span>
  <span class="social" style="left:240px"></span>
  <span class="social" style="left:287px"></span>
  <div class="fcol" style="left:394px"><h3>QUICK LINKS</h3><ul><li>HOME</li><li>ABOUT US</li><li>SERVICES</li><li>SOLUTIONS</li><li>SECTORS</li><li>CASE STUDIES</li><li>MORE</li></ul></div>
  <div class="fcol" style="left:563px"><h3>OUR POLICIES</h3><ul><li>TERMS &amp; CONDITIONS</li><li>PRIVACY POLICY</li><li>COMPANY VALUES</li><li>CORPORATE ETHICS POLICY</li><li>ANTI SLAVERY POLICY</li></ul></div>
  <div class="fcol" style="left:783px"><h3>SUPPORT</h3><ul><li>TEAM</li><li>ABOUT US</li><li>CAREERS</li><li>OUR VALUES</li></ul></div>
  <div class="fcol" style="left:952px"><h3>LINK</h3><ul><li>FAQ'S</li><li>TERMS &amp; CONDITIONS</li><li>PRIVACY POLICY</li><li>SITE MAP</li><li>COOKIES POLICY</li></ul></div>
  <div class="to-top"><svg width="14" height="10" viewBox="0 0 14 10"><path d="M1 8l6-6 6 6" stroke="#1b3482" stroke-width="2" fill="none"/></svg></div>
  <div class="legal" style="left:109px">Copyright © 2022 | All Rights Reserved</div>
  <div class="legal" style="left:809px">TERMS &amp; CONDITIONS&nbsp;&nbsp;&nbsp;&nbsp;&nbsp;&nbsp;|&nbsp;&nbsp;&nbsp;&nbsp;&nbsp;&nbsp;PRIVACY POLICY</div>
</footer>

</body>
</html>
```